KVO-Business Card Design

I need a modern, professional business card design that includes my logo as the main feature, maybe the entire background with the contact info overlaying or even contact info on the back and the logo full frontal

Neat and organized placement of contact information

Would like to see options in black and white

Target Market(s)

real estate Developers, Construction managers, business and home owners

Industry/Entity Type

Construction

Contact Information for Business Card

KVO Construction
Danny Ferrante
General Contractor

Office: 1-888-902-7315 Ext #1
Cell: 215-730-4162
Fax: 1-888-902-7315

Font styles to use
Serif

Requirements
Must have
• title
• office #
• cell #
• Email
• website
Nice to have
• fax

```html
<!DOCTYPE html>
<html lang="en">
<head>
<meta charset="utf-8">
<title>KVO Construction – Business Card</title>
<link href="https://fonts.googleapis.com/css2?family=Arimo:wght@400;700&display=swap" rel="stylesheet">
<style>
  :root {
    --backdrop: #3a3a3c;
    --card-black: #050505;
    --card-white: #f2f4f5;
    --brand-green: #2e8b2e;
    --brand-green-light: #6cc04a;
    --ink-grey: #555a5c;
    --ink-light: #d8d8d8;
  }
  * { margin: 0; padding: 0; box-sizing: border-box; }
  html, body { width: 1200px; height: 810px; overflow: hidden; }
  body {
    background: var(--backdrop);
    font-family: "Arimo", Arial, sans-serif;
    position: relative;
  }
  .card {
    position: absolute;
    width: 580px;
    height: 330px;
    border-radius: 22px;
    box-shadow: 0 8px 24px rgba(0,0,0,.45);
  }
  .card-front {
    left: 70px; top: 60px;
    background: var(--card-black);
    display: flex; flex-direction: column; align-items: center; justify-content: center;
  }
  .card-front .brand-name {
    font-size: 46px; font-weight: 700; color: var(--brand-green-light);
    letter-spacing: 1px;
  }
  .card-front .brand-mark {
    width: 26px; height: 26px; background: var(--brand-green-light);
    margin-bottom: 18px;
  }
  .card-front .web {
    margin-top: 26px; font-size: 15px; color: var(--ink-light); letter-spacing: .5px;
  }
  .card-back {
    left: 550px; top: 420px;
    background: var(--card-white);
  }
  .card-back .brand-name {
    position: absolute; left: 40px; top: 48px;
    font-size: 30px; font-weight: 700; color: var(--brand-green);
    width: 240px; line-height: 1.1;
  }
  .card-back .person {
    position: absolute; right: 36px; top: 44px; text-align: right;
  }
  .person .name {
    font-size: 21px; color: var(--brand-green); letter-spacing: 1px; text-transform: uppercase;
  }
  .person .title {
    margin-top: 4px; font-size: 14px; color: var(--ink-grey);
  }
  .contact-list {
    position: absolute; left: 40px; bottom: 26px; list-style: none;
  }
  .contact-list li {
    display: flex; align-items: center; gap: 8px;
    font-size: 15px; color: var(--ink-grey); line-height: 23px;
  }
  .contact-list svg { width: 13px; height: 13px; fill: var(--brand-green); flex: none; }
  .contact-list .web-accent { color: var(--brand-green); }
</style>
</head>
<body>
  <section class="card card-front">
    <div class="brand-mark"></div>
    <div class="brand-name">KVO Construction</div>
    <div class="web">www.KVOConstruction.com</div>
  </section>

  <section class="card card-back">
    <div class="brand-name">KVO Construction</div>
    <div class="person">
      <div class="name">Danny Ferrante</div>
      <div class="title">General Contractor</div>
    </div>
    <ul class="contact-list">
      <li><svg viewBox="0 0 16 16"><path d="M3 1l3 3-2 2c1 2 4 5 6 6l2-2 3 3-2 2C7 15 1 9 1 3z"/></svg>1-888-902-7315 Ext #1</li>
      <li><svg viewBox="0 0 16 16"><path d="M4 0h8v16H4zM5.5 2v10h5V2z"/></svg>215-730-4162</li>
      <li><svg viewBox="0 0 16 16"><path d="M4 1h8v4H4zM1 6h14v7h-3v2H4v-2H1zM5 10v4h6v-4z"/></svg>1-888-902-7315</li>
      <li><svg viewBox="0 0 16 16"><path d="M0 3h16v1L8 9 0 4zM0 6l8 5 8-5v7H0z"/></svg>support@KVOConstruction.com</li>
      <li><svg viewBox="0 0 16 16"><circle cx="8" cy="8" r="7" fill="none" stroke="#2e8b2e" stroke-width="1.6"/><path d="M1 8h14M8 1c-4 4-4 10 0 14M8 1c4 4 4 10 0 14" fill="none" stroke="#2e8b2e" stroke-width="1.2"/></svg>www.<span class="web-accent">KVOConstruction</span>.com</li>
    </ul>
  </section>
</body>
</html>
```